Branding Package for an environmental water treatment operations company
Use the provided Logo. The name of the company is Coordinated Ecological Solutions or CES
Branding Package for an environmental water treatment operations company - Environment
Creative Brief
Professional
Mark Delane
President
217 Thornbury Ave Halden Falls, OH. 44318
tkvallen@mailbrook.net
U have freedom to experiment with any fonts to find the best match.
I will add to this later as I see what's being submitted.

```html
<!DOCTYPE html>
<html lang="en">
<head>
<meta charset="utf-8">
<title>Coordinated Ecological Solutions – Business Cards</title>
<link rel="stylesheet" href="https://fonts.googleapis.com/css2?family=Cormorant+Garamond:wght@500;600&display=swap">
<style>
  :root {
    --backdrop: #e9e7e2;
    --card: #ffffff;
    --card-edge: #dcdcdc;
    --accent: #2b6db3;
    --ink: #4e4e4e;
    --ink-soft: #8a8a8a;
    --rule: #b9b9b9;
    --mark-dot: #a3abb0;
  }
  * { box-sizing: border-box; margin: 0; padding: 0; }
  html, body { width: 1200px; height: 1023px; overflow: hidden; }
  body {
    background: var(--backdrop);
    display: flex;
    align-items: center;
    justify-content: center;
    gap: 44px;
  }
  .card {
    width: 540px;
    height: 309px;
    background: var(--card);
    border: 1px solid var(--card-edge);
    box-shadow: 0 6px 18px rgba(0,0,0,0.12);
    position: relative;
  }
  .brand { display: flex; align-items: center; gap: 10px; }
  .brand-dot { border-radius: 50%; background: var(--mark-dot); flex: none; }
  .brand-name {
    font-family: "Cormorant Garamond", serif;
    font-weight: 600;
    color: var(--ink);
    letter-spacing: 0.5px;
    line-height: 1;
    white-space: nowrap;
  }

  /* Details side */
  .card-details .brand { position: absolute; left: 34px; bottom: 38px; }
  .card-details .brand-dot { width: 16px; height: 16px; }
  .card-details .brand-name { font-size: 17px; }

  .contact {
    position: absolute;
    right: 34px;
    top: 40px;
    width: 250px;
    padding-left: 20px;
    border-left: 1px solid var(--rule);
    font-family: "Cormorant Garamond", serif;
    color: var(--ink);
    text-transform: uppercase;
    letter-spacing: 1.4px;
  }
  .contact-name { font-size: 17px; font-weight: 600; color: var(--accent); }
  .contact-title { font-size: 12px; font-weight: 500; color: var(--ink-soft); margin-bottom: 24px; }
  .contact-block { margin-bottom: 14px; }
  .contact-line { font-size: 11.5px; font-weight: 500; line-height: 1.6; display: flex; align-items: center; gap: 7px; }
  .contact-line svg { width: 10px; height: 10px; flex: none; fill: var(--accent); }
  .contact-email { text-transform: none; }

  /* Logo side */
  .card-logo { display: flex; align-items: center; justify-content: center; }
  .card-logo .brand-dot { width: 24px; height: 24px; }
  .card-logo .brand-name { font-size: 26px; }
</style>
</head>
<body>

  <section class="card card-details" aria-label="Business card, contact side">
    <div class="contact">
      <p class="contact-name">Mark Delane</p>
      <p class="contact-title">President</p>
      <div class="contact-block">
        <p class="contact-line">217 Thornbury Ave</p>
        <p class="contact-line">Halden Falls, OH. 44318</p>
      </div>
      <div class="contact-block">
        <p class="contact-line">
          <svg viewBox="0 0 10 10" aria-hidden="true"><path d="M2 0.5h2l0.6 2.4-1.2 0.8a5.5 5.5 0 0 0 2.9 2.9l0.8-1.2 2.4 0.6v2a1 1 0 0 1-1 1A8.5 8.5 0 0 1 1 1.5a1 1 0 0 1 1-1z"/></svg>
          (555) 014-0148
        </p>
        <p class="contact-line">
          <svg viewBox="0 0 10 10" aria-hidden="true"><rect x="2.5" y="0.5" width="5" height="9" rx="1"/></svg>
          (555) 014-0192
        </p>
        <p class="contact-line">
          <svg viewBox="0 0 10 10" aria-hidden="true"><path d="M0.5 2h9v6h-9z M0.5 2l4.5 3.5 4.5-3.5" fill="none" stroke="#2b6db3" stroke-width="1"/></svg>
          <span class="contact-email">tkvallen@mailbrook.net</span>
        </p>
      </div>
    </div>
    <div class="brand">
      <span class="brand-dot"></span>
      <span class="brand-name">Coordinated Ecological Solutions</span>
    </div>
  </section>

  <section class="card card-logo" aria-label="Business card, name side">
    <div class="brand">
      <span class="brand-dot"></span>
      <span class="brand-name">Coordinated Ecological Solutions</span>
    </div>
  </section>

</body>
</html>
```